Business Card Design Project

I need a business card designed for TalePorter, a website which has people share their fictional story ideas with others. The business cards should incorporate the websites's logo, which can be found at www.taleporter-demo.net .

Target Market(s)

These will be primarily used in business development activities, not given to customers. It therefore needs to have a clean, professional appearance, and yet communicate what the company is trying to achieve as a bold startup.

Industry/Entity Type

Business

```html
<!DOCTYPE html>
<html lang="en">
<head>
<meta charset="utf-8">
<title>TalePorter Business Card</title>
<link rel="stylesheet" href="https://fonts.googleapis.com/css2?family=Michroma&family=Tenor+Sans&family=Arimo:wght@400&family=Montserrat:wght@500&display=swap">
<style>
  :root {
    --stage: #9c9c9c;
    --card-navy: #1f5080;
    --arc-blue: #3f86b7;
    --back-pattern-top: #285b8b;
    --back-band: #1c4872;
    --back-pattern-bottom: #2e6495;
    --badge-fill: #dce9f4;
    --badge-icon: #275b8c;
    --ink-light: #ffffff;
    --ink-soft: #e3edf6;
  }
  * { margin: 0; padding: 0; box-sizing: border-box; }
  html, body {
    width: 1200px; height: 1200px; overflow: hidden;
    background: var(--stage);
  }
  .sheet { position: relative; width: 1200px; height: 1200px; }
  .card {
    position: absolute; left: 180px; width: 840px; height: 480px;
    overflow: hidden;
    box-shadow: 0 6px 18px rgba(0,0,0,0.25);
  }
  .card-front { top: 90px; background: var(--card-navy); }
  .card-back { top: 630px; background: var(--back-band); }

  /* Front */
  .front-arc {
    position: absolute; left: -295px; top: -32px;
    width: 544px; height: 544px; border-radius: 50%;
    background: var(--arc-blue);
  }
  .holder-name {
    position: absolute; left: 420px; top: 36px;
    font-family: "Michroma", sans-serif; font-size: 40px;
    color: var(--ink-light); letter-spacing: 1px;
  }
  .holder-title {
    position: absolute; left: 424px; top: 96px;
    font-family: "Tenor Sans", sans-serif; font-size: 24px;
    color: var(--ink-soft);
  }
  .contact-list {
    position: absolute; left: 280px; top: 372px; list-style: none;
    font-family: "Arimo", sans-serif; font-size: 25px; color: var(--ink-light);
  }
  .contact-list li { display: flex; align-items: center; gap: 8px; height: 34px; }
  .contact-list svg { width: 20px; height: 20px; }

  /* Back */
  .back-pattern-top {
    position: absolute; left: 0; top: 0; width: 100%; height: 116px;
    background: var(--back-pattern-top);
  }
  .back-band {
    position: absolute; left: 0; top: 116px; width: 100%; height: 194px;
    background: var(--back-band);
  }
  .back-pattern-bottom {
    position: absolute; left: 0; top: 310px; width: 100%; height: 170px;
    background: var(--back-pattern-bottom);
  }
  .brand-name {
    position: absolute; left: 0; top: 146px; width: 100%; text-align: center;
    font-family: "Montserrat", sans-serif; font-weight: 500; font-size: 76px;
    color: var(--ink-light); line-height: 1;
  }
  .brand-site {
    position: absolute; left: 0; top: 248px; width: 100%;
    display: flex; justify-content: center; align-items: center; gap: 8px;
    font-family: "Arimo", sans-serif; font-size: 24px; color: var(--ink-light);
  }
  .brand-site svg { width: 18px; height: 18px; }
  .badge {
    position: absolute; top: 343px; width: 108px; height: 108px;
    border-radius: 50%; background: var(--badge-fill);
    display: flex; align-items: center; justify-content: center;
  }
  .badge svg { width: 56px; height: 56px; }
  .badge-write { left: 194px; }
  .badge-chat { left: 368px; }
  .badge-star { left: 544px; }
</style>
</head>
<body>
<main class="sheet">
  <section class="card card-front" aria-label="Card front">
    <div class="front-arc"></div>
    <h1 class="holder-name">Martin Hale</h1>
    <p class="holder-title">Managing Director</p>
    <ul class="contact-list">
      <li>
        <svg viewBox="0 0 20 20" aria-hidden="true"><rect x="6" y="1" width="8" height="18" rx="2" fill="none" stroke="#fff" stroke-width="2"/><circle cx="10" cy="15.5" r="1.2" fill="#fff"/></svg>
        0-000-000-000
      </li>
      <li>
        <svg viewBox="0 0 20 20" aria-hidden="true"><rect x="2" y="5" width="16" height="11" fill="none" stroke="#fff" stroke-width="2"/><path d="M2 5 L10 11 L18 5" fill="none" stroke="#fff" stroke-width="2"/></svg>
        hello@mailbox-demo.com
      </li>
    </ul>
  </section>

  <section class="card card-back" aria-label="Card back">
    <div class="back-pattern-top" role="img" aria-label="Woven line pattern texture in blue tones"></div>
    <div class="back-band"></div>
    <div class="back-pattern-bottom" role="img" aria-label="Woven line pattern texture in blue tones"></div>
    <h2 class="brand-name">TalePorter</h2>
    <p class="brand-site">
      <svg viewBox="0 0 20 20" aria-hidden="true"><circle cx="10" cy="10" r="8" fill="none" stroke="#fff" stroke-width="2"/><path d="M2 10 H18 M10 2 C6 6 6 14 10 18 M10 2 C14 6 14 14 10 18" fill="none" stroke="#fff" stroke-width="1.5"/></svg>
      www.taleporter-demo.net
    </p>
    <div class="badge badge-write">
      <svg viewBox="0 0 56 56" aria-hidden="true"><path d="M30 12 H10 V46 H44 V26" fill="none" stroke="var(--badge-icon)" stroke-width="4" stroke-linejoin="round"/><path d="M24 34 L27 25 L44 8 L50 14 L33 31 Z" fill="var(--badge-icon)"/></svg>
    </div>
    <div class="badge badge-chat">
      <svg viewBox="0 0 56 56" aria-hidden="true"><path d="M8 14 H34 V32 H18 L11 38 V32 H8 Z" fill="none" stroke="var(--badge-icon)" stroke-width="4" stroke-linejoin="round"/><path d="M38 22 H48 V40 H45 V46 L38 40 H22 V36" fill="none" stroke="var(--badge-icon)" stroke-width="4" stroke-linejoin="round"/></svg>
    </div>
    <div class="badge badge-star">
      <svg viewBox="0 0 56 56" aria-hidden="true"><path d="M28 7 L34 21 L49 22 L38 32 L41 47 L28 39 L15 47 L18 32 L7 22 L22 21 Z" fill="none" stroke="var(--badge-icon)" stroke-width="4" stroke-linejoin="round"/></svg>
    </div>
  </section>
</main>
</body>
</html>
```